Folder & Business Card for Automation Company
Brightwell Torque Mfr.
Folder & Business Card for Automation Company - Manufacturing
Creative Brief
Professional
Darren Okafor
Vice President
4817 Halvern Road Merriam, KS 66209
do@brightwelltorquemfr.example
www.brightwelltorquemfr.example
Along with a business card we are looking for a design for the front cover of a folder to be used for sales literature. The cover should also include our logo.

```html
<!DOCTYPE html>
<html lang="en">
<head>
<meta charset="utf-8">
<title>Brightwell Torque Mfr. — Folder Cover</title>
<link rel="stylesheet" href="https://fonts.googleapis.com/css2?family=Cinzel:wght@400;700&display=swap">
<style>
  :root {
    --backdrop: #ece9e4;
    --paper: #ffffff;
    --fold-line: #d9d9d9;
    --brand-red: #d6262b;
    --brand-red-deep: #a8161b;
    --band-dark: #2b2b2c;
    --band-mid: #3f3f41;
    --ink: #222223;
    --band-text: #e6e6e6;
  }
  * { margin: 0; padding: 0; box-sizing: border-box; }
  html, body { width: 1200px; height: 871px; overflow: hidden; }
  body { background: var(--backdrop); position: relative; font-family: "Cinzel", serif; }

  .folder {
    position: absolute; left: 50px; top: 45px; width: 1100px; height: 780px;
    display: flex; box-shadow: 0 2px 10px rgba(0,0,0,.12);
  }
  .folder-panel { position: relative; width: 550px; height: 100%; background: var(--paper); }
  .folder-panel--inside { border-right: 1px solid var(--fold-line); }

  .brand {
    position: absolute; top: 338px; left: 0; width: 100%;
    display: flex; align-items: center; justify-content: center; gap: 12px;
  }
  .brand-dot { width: 18px; height: 18px; border-radius: 50%; background: var(--brand-red); flex: none; }
  .brand-name {
    font-family: "Cinzel", serif; font-weight: 700; font-size: 30px;
    letter-spacing: 1px; color: var(--ink); line-height: 1;
  }

  .cover-band { position: absolute; left: 0; bottom: 0; width: 550px; height: 140px; }
  .cover-band svg { display: block; }

  .contact {
    position: absolute; left: 0; bottom: 12px; width: 100%;
    color: var(--band-text); font-size: 9.5px; letter-spacing: .4px;
    display: flex; flex-direction: column; align-items: center; gap: 6px;
  }
  .contact-row { display: flex; gap: 12px; }
  .contact-item { display: flex; align-items: center; gap: 4px; white-space: nowrap; }
  .contact-icon { width: 9px; height: 9px; border-radius: 50%; background: var(--brand-red); flex: none; }
</style>
</head>
<body>
  <main class="folder">
    <section class="folder-panel folder-panel--inside" aria-label="Inside flap"></section>

    <section class="folder-panel folder-panel--cover" aria-label="Front cover">
      <div class="brand">
        <span class="brand-dot"></span>
        <span class="brand-name">Brightwell Torque Mfr.</span>
      </div>

      <div class="cover-band">
        <svg width="550" height="140" viewBox="0 0 550 140">
          <defs>
            <linearGradient id="band-fill" x1="0" y1="0" x2="0" y2="1">
              <stop offset="0" stop-color="var(--band-mid)"/>
              <stop offset="1" stop-color="var(--band-dark)"/>
            </linearGradient>
          </defs>
          <path d="M0 20 C120 0 230 50 360 42 C450 36 510 20 550 14 L550 80 L0 80 Z" fill="var(--brand-red)"/>
          <path d="M0 34 C140 18 250 62 380 58 C460 55 520 42 550 38 L550 80 L0 80 Z" fill="var(--brand-red-deep)" opacity=".7"/>
          <path d="M0 50 C140 38 260 72 390 68 C470 66 520 58 550 54 L550 140 L0 140 Z" fill="url(#band-fill)"/>
        </svg>
        <div class="contact">
          <div class="contact-row">
            <span class="contact-item"><span class="contact-icon"></span>4817 Halvern Road Merriam, KS 66209</span>
            <span class="contact-item"><span class="contact-icon"></span>913-555-0148</span>
            <span class="contact-item"><span class="contact-icon"></span>913-555-0162</span>
          </div>
          <div class="contact-row">
            <span class="contact-item"><span class="contact-icon"></span>do@brightwelltorquemfr.example</span>
            <span class="contact-item"><span class="contact-icon"></span>www.brightwelltorquemfr.example</span>
          </div>
        </div>
      </div>
    </section>
  </main>
</body>
</html>
```